Dorrie's Letterhead

Letterhead should say: Dorrie Fenwick Childern's Book Author/Illustrator

Font should be fun and colorful, but not so distracting that it over shadows the letters content. My business card is shaped like a bone so I would like to keep that shape somewhere in the theme of the letterhead. You can find my book on Bookvale Wiggo and the Silver Kite if you would like to get a sense of my artistic style.
Updates

While I did say I want to carry out the bone theme. Don't be afraid to expand on that example: book shaped like a bone, paint brush...really go for it.

Surprise me! Good luck

Target Market(s)

Adults buying my book

Industry/Entity Type

Business

Requirements
Must have
• Fun colorful
Should not have
• Only one color

```html
<!DOCTYPE html>
<html lang="en">
<head>
<meta charset="utf-8">
<title>Dorrie Fenwick Letterhead</title>
<link rel="stylesheet" href="https://fonts.googleapis.com/css2?family=Nunito:wght@900&family=Gochi+Hand&family=Arimo:wght@700&display=swap">
<style>
  :root {
    --backdrop: #f4f4f4;
    --paper: #ffffff;
    --paper-edge: #555555;
    --ink: #1c1c1c;
    --name-purple: #7b2a90;
    --label-orange: #f04e23;
    --label-blue: #1e9ad6;
    --label-magenta: #d4137f;
  }
  html, body {
    margin: 0;
    padding: 0;
    width: 950px;
    height: 1200px;
    overflow: hidden;
    background: var(--backdrop);
  }
  .letterhead {
    position: absolute;
    left: 15px;
    top: 20px;
    width: 920px;
    height: 1160px;
  }
  .letterhead__sheet {
    position: absolute;
    inset: 0;
    width: 920px;
    height: 1160px;
  }
  .letterhead__sheet path {
    fill: var(--paper);
    stroke: var(--paper-edge);
    stroke-width: 1;
  }
  .brand {
    position: absolute;
    left: 468px;
    top: 40px;
    width: 360px;
  }
  .brand__name {
    margin: 0;
    font-family: "Nunito", sans-serif;
    font-weight: 900;
    font-size: 38px;
    line-height: 1;
    letter-spacing: 0.5px;
    color: var(--name-purple);
  }
  .brand__tagline {
    margin: 6px 0 0 2px;
    font-family: "Gochi Hand", cursive;
    font-size: 23px;
    line-height: 1;
    color: var(--ink);
  }
  .contact {
    position: absolute;
    left: 110px;
    top: 1106px;
    margin: 0;
    font-family: "Arimo", sans-serif;
    font-weight: 700;
    font-size: 10px;
    color: var(--ink);
    white-space: nowrap;
  }
  .contact__item { margin-right: 16px; }
  .contact__label {
    font-family: "Gochi Hand", cursive;
    font-weight: 400;
    font-size: 13px;
    margin-right: 4px;
  }
  .contact__label--cell { color: var(--label-orange); }
  .contact__label--email { color: var(--label-blue); }
  .contact__label--address { color: var(--label-magenta); }
</style>
</head>
<body>
  <main class="letterhead">
    <svg class="letterhead__sheet" viewBox="0 0 920 1160" aria-hidden="true">
      <path d="M0.5,32 A58 58 0 0 0 106 0.5 A54 43 0 0 0 214 0.5 L919.5,0.5 L919.5,1159.5 L0.5,1159.5 Z"/>
    </svg>

    <header class="brand">
      <h1 class="brand__name">Dorrie Fenwick</h1>
      <p class="brand__tagline">children's book author/illustrator</p>
    </header>

    <footer>
      <p class="contact">
        <span class="contact__item"><span class="contact__label contact__label--cell">cell:</span>(555) 214 7730</span>
        <span class="contact__item"><span class="contact__label contact__label--email">email:</span>wiggoskite@inkmail.net</span>
        <span class="contact__item"><span class="contact__label contact__label--address">address:</span>xxxxx Ut alis nos eraesequatis nibh elestrud mincil del ut lore magna feuisit</span>
      </p>
    </footer>
  </main>
</body>
</html>
```